Business Card Design

Electronic Security Installation Specialists

Check out our website at www.brightpulsellc.com to see what we do.

Industry/Entity Type

Business

Contact Information for Business Card

Bright Pulse
Marianne Tolbert
218 Orchard Bend
Millbrookton, OH 44871

Colors
3176b5
0455a3
ffffff

```html
<!DOCTYPE html>
<html lang="en">
<head>
<meta charset="utf-8">
<title>Bright Pulse — Business Card</title>
<link href="https://fonts.googleapis.com/css2?family=Fira+Sans:wght@700&family=Oswald:wght@500&display=swap" rel="stylesheet">
<style>
  :root {
    --backdrop: #ececec;
    --card-white: #fbfbfb;
    --name-blue: #8cc6e6;
    --address-grey: #b4b4b4;
    --card-blue-light: #6ab8e2;
    --card-blue: #4aa3d6;
    --card-blue-deep: #3d96cc;
    --tagline-white: #ffffff;
  }
  * { margin: 0; padding: 0; box-sizing: border-box; }
  html, body {
    width: 1200px;
    height: 723px;
    overflow: hidden;
    background: var(--backdrop);
  }
  .card-set {
    position: relative;
    width: 1200px;
    height: 723px;
    display: flex;
    align-items: center;
    justify-content: center;
    gap: 60px;
  }
  .card {
    position: relative;
    width: 520px;
    height: 297px;
    border-radius: 3px;
    box-shadow: 0 6px 18px rgba(0, 0, 0, 0.12), 0 1px 3px rgba(0, 0, 0, 0.08);
    overflow: hidden;
  }
  .card--contact {
    background: var(--card-white);
  }
  .contact {
    position: absolute;
    left: 68px;
    top: 82px;
    font-family: "Fira Sans", Arial, sans-serif;
    font-weight: 700;
  }
  .contact__name {
    color: var(--name-blue);
    font-size: 34px;
    letter-spacing: 1px;
    line-height: 1.1;
    margin-bottom: 8px;
  }
  .contact__address {
    font-style: normal;
    color: var(--address-grey);
    font-size: 20px;
    line-height: 1.3;
    letter-spacing: 0.5px;
    padding-left: 26px;
  }
  .card--brand {
    background: linear-gradient(160deg, var(--card-blue-light) 0%, var(--card-blue) 55%, var(--card-blue-deep) 100%);
  }
  .brand-name {
    position: absolute;
    right: 30px;
    bottom: 28px;
    font-family: "Oswald", "Arial Narrow", sans-serif;
    font-weight: 500;
    font-size: 24px;
    letter-spacing: 3px;
    text-transform: uppercase;
    color: var(--tagline-white);
    opacity: 0.9;
  }
</style>
</head>
<body>
  <main class="card-set">
    <section class="card card--contact" aria-label="Card front with contact details">
      <div class="contact">
        <h1 class="contact__name">Marianne Tolbert</h1>
        <address class="contact__address">
          218 Orchard Bend<br>
          Millbrookton,<br>
          OH 44871
        </address>
      </div>
    </section>
    <section class="card card--brand" aria-label="Card back with company name">
      <p class="brand-name">Bright Pulse</p>
    </section>
  </main>
</body>
</html>
```